Mirelo Japanese Restaurant

We just want the japanese sakura background and the menu as below

Side dish :
Edamame $4
Japanese Steam Green Bean
Crab Craw $3 each
With Japanese mayo
Teriyaki Chicken stick $3 each
Chicken stick with home made teriyaki sauce
Tempura Prawns $7
With Japanese mayo
Miso Soup $3
Traditional Japanese soup
Salt and Pepper Calamari $7
With japanese mayo

Main dish:
Gyu Don $12
Bowl of steam rice topped with beef and onion simmered in a mildly sweet sauce.
Teriyaki Don $12
Bowl of steam rice topped with your choice of beef, chicken or pork and with our special Teriyaki sauce.
Vege Don $12
Bowl of steam rice with seasonal Vegetables with the special japanese sweet soy sauce.
Japanese Curry $12,(prawns $14)
Bowl of steam rice with Chicken, pork or prawn with japanese mild curry sauce.
Katsu Don $12
Bowl of steam rice topped with a deep-fried pork cutlet and egg with the japanese special sauce.
Oyako Don $12
Bowl of steam rice topped with chick and egg with japanese special sauce.
Spice Don $12
Bowl of steam rice topped with beef or chicken with japanese spice sauce.
Gingle Don $12
Bowl of steam rice topped with beef or chicken with japanese ginger sauce.
Sushi $3
Roll everyday on seasonal
ingredient.

Japanese-style sweets
Black Sesame Ice cream $4.5
Green tea Ice cream $4.5

```html
<!DOCTYPE html>
<html lang="en">
<head>
<meta charset="utf-8">
<title>Mirelo Japanese Restaurant – Menu</title>
<link rel="stylesheet" href="https://fonts.googleapis.com/css2?family=Kaushan+Script&family=Arvo:wght@400;700&display=swap">
<style>
:root{
  --canvas:#ffffff;
  --panel:#effbfd;
  --panel-border:#8a8a8a;
  --ink:#141414;
  --blossom:#e7a6cf;
  --blossom-faint:rgba(226,170,205,0.32);
  --branch-faint:rgba(170,130,125,0.22);
  --banner-a:#f2cdd6;
  --banner-b:#fbeff1;
  --seal:#e98aa8;
  --scroll-a:#d9d2d3;
  --scroll-b:#f4eef0;
}
*{box-sizing:border-box;margin:0;padding:0}
html,body{width:853px;height:1200px;overflow:hidden;background:var(--canvas)}
.canvas{position:relative;width:853px;height:1200px}
.panel{position:absolute;width:376px;height:535px;background:var(--panel);overflow:hidden}
.panel--bordered{border:1px solid var(--panel-border)}
.panel--cover{left:4px;top:0}
.panel--sides{left:472px;top:0}
.panel--mains{left:4px;top:662px}
.panel--sweets{left:472px;top:662px}

.blossoms{position:absolute}
.blossoms--bold{background:radial-gradient(ellipse at 55% 50%,var(--blossom) 0%,rgba(231,166,207,.55) 45%,rgba(239,251,253,0) 75%)}
.blossoms--faint{background:radial-gradient(ellipse at 50% 50%,var(--blossom-faint) 0%,var(--branch-faint) 40%,rgba(239,251,253,0) 72%)}

.banner{position:absolute;left:0;top:216px;width:376px;height:102px;
  background:linear-gradient(90deg,var(--banner-a),var(--banner-b) 60%,var(--banner-a));
  border-top:1px solid #c9b5b9;border-bottom:1px solid #c9b5b9}
.banner__seal{position:absolute;left:10px;top:22px;width:56px;height:56px;border-radius:50%;background:var(--seal)}
.banner__name{position:absolute;left:78px;top:10px;width:210px;font-family:"Kaushan Script",cursive;
  font-weight:400;color:var(--ink);text-align:center;line-height:1.15}
.banner__name span{display:block}
.banner__name .big{font-size:34px}
.banner__name .small{font-size:20px}
.banner__scroll{position:absolute;right:0;top:0;width:82px;height:100px;
  background:linear-gradient(160deg,var(--scroll-b),var(--scroll-a));border-left:1px solid #b8aaac}

.heading{position:absolute;font-family:"Kaushan Script",cursive;font-weight:400;font-size:42px;color:var(--ink);line-height:1;white-space:nowrap}

.item{position:absolute;font-family:"Arvo",serif;color:var(--ink)}
.item__row{display:flex;align-items:baseline;font-size:14.5px;line-height:18px;white-space:nowrap}
.item__leader{flex:1;border-bottom:2px dotted var(--ink);margin:0 2px;transform:translateY(-3px)}
.item__note{font-size:10.5px;line-height:13px;margin-top:1px;padding-left:1px}
</style>
</head>
<body>
<div class="canvas">

  <section class="panel panel--cover">
    <div class="blossoms blossoms--bold" style="left:60px;top:0;width:316px;height:205px" role="img" aria-label="Cherry blossom branch with pink flowers"></div>
    <div class="banner">
      <div class="banner__seal"></div>
      <div class="banner__name"><span class="big">Mirelo</span><span class="small">Japanese Restaurant</span></div>
      <div class="banner__scroll" role="img" aria-label="Ink painting of a blossoming tree"></div>
    </div>
    <div class="blossoms blossoms--bold" style="left:0;top:330px;width:300px;height:205px" role="img" aria-label="Cherry blossom branch with pink flowers"></div>
  </section>

  <section class="panel panel--sides panel--bordered">
    <div class="blossoms blossoms--faint" style="left:150px;top:0;width:226px;height:260px" role="img" aria-label="Faint cherry blossom branch"></div>
    <div class="blossoms blossoms--faint" style="left:0;top:300px;width:230px;height:235px" role="img" aria-label="Faint cherry blossom branch"></div>
    <h2 class="heading" style="left:44px;top:4px">Side Dish</h2>

    <div class="item" style="left:26px;top:61px;width:223px">
      <div class="item__row">Edamame<span class="item__leader"></span>$4</div>
      <div class="item__note">(Japanese steam green bean)</div>
    </div>
    <div class="item" style="left:26px;top:105px;width:223px">
      <div class="item__row">Crab Claw<span class="item__leader"></span>$3</div>
      <div class="item__note">(with Japanese mayo)</div>
    </div>
    <div class="item" style="left:26px;top:151px;width:223px">
      <div class="item__row">Tempura Prawns<span class="item__leader"></span>$7</div>
      <div class="item__note">(with Japanese mayo)</div>
    </div>
    <div class="item" style="left:26px;top:195px;width:223px">
      <div class="item__row">Miso Soup<span class="item__leader"></span>$3</div>
      <div class="item__note">(Traditional Japanese Soup)</div>
    </div>
    <div class="item" style="left:26px;top:242px;width:223px">
      <div class="item__row">Salt &amp; Pepper Calamari<span class="item__leader"></span>$7</div>
      <div class="item__note">(with Japanese mayo)</div>
    </div>

    <h2 class="heading" style="left:28px;top:278px">Main Dish</h2>

    <div class="item" style="left:26px;top:333px;width:226px">
      <div class="item__row">GyuDon<span class="item__leader"></span>$12</div>
      <div class="item__note">(bowl of steamed rice toped with beef<br>&amp; onion simmered in a mildly sweet<br>sauce)</div>
    </div>
    <div class="item" style="left:28px;top:409px;width:262px">
      <div class="item__row">TeriyakiDon<span class="item__leader"></span>$12</div>
      <div class="item__note">(bowl of steamed rice topped with your<br>choice of beef, chicken or pork &amp; with<br>our special teriyaki sauce)</div>
    </div>
  </section>

  <section class="panel panel--mains panel--bordered">
    <div class="blossoms blossoms--faint" style="left:160px;top:0;width:216px;height:260px" role="img" aria-label="Faint cherry blossom branch"></div>
    <div class="blossoms blossoms--faint" style="left:0;top:330px;width:300px;height:205px" role="img" aria-label="Faint cherry blossom branch"></div>

    <div class="item" style="left:14px;top:56px;width:312px">
      <div class="item__row">Japanese curry<span class="item__leader"></span>$12</div>
      <div class="item__row">with prawn<span class="item__leader"></span>$14</div>
      <div class="item__note">(bowl of steamed rice with chicken,<br>pork or prawn with Japanese mild<br>curry sauce)</div>
    </div>
    <div class="item" style="left:14px;top:142px;width:312px">
      <div class="item__row">KatsuDon<span class="item__leader"></span>$12</div>
      <div class="item__note">(bowl of steamed rice topped with<br>a deep-fried pork cutlet and egg<br>with Japanese special sauce)</div>
    </div>
    <div class="item" style="left:19px;top:219px;width:272px">
      <div class="item__row">OyakoDon<span class="item__leader"></span>$12</div>
      <div class="item__note">(bowl of steamed rice topped with<br>chicken and egg with Japanese<br>special sauce)</div>
    </div>
    <div class="item" style="left:19px;top:295px;width:272px">
      <div class="item__row">SpiceDon<span class="item__leader"></span>$12</div>
      <div class="item__note">(bowl of steamed rice topped with<br>beef or chicken with Japanese<br>spice sauce)</div>
    </div>
    <div class="item" style="left:19px;top:373px;width:272px">
      <div class="item__row">GingleDon<span class="item__leader"></span>$12</div>
      <div class="item__note">(bowl of steamed rice topped with<br>beef or chicken with Japanese<br>ginger sauce)</div>
    </div>
    <div class="item" style="left:19px;top:457px;width:272px">
      <div class="item__row">Sushi<span class="item__leader"></span>$3</div>
      <div class="item__note">(Roll everyday on seasonal<br>ingredients)</div>
    </div>
  </section>

  <section class="panel panel--sweets panel--bordered">
    <div class="blossoms blossoms--faint" style="left:60px;top:30px;width:316px;height:150px" role="img" aria-label="Faint cherry blossom branch"></div>
    <div class="blossoms blossoms--faint" style="left:0;top:330px;width:376px;height:205px" role="img" aria-label="Faint cherry blossom branch"></div>
    <h2 class="heading" style="left:8px;top:8px;font-size:40px">Japanese Sweets</h2>

    <div class="item" style="left:20px;top:110px;width:266px">
      <div class="item__row">Black Sesame Ice cream<span class="item__leader"></span>$4.5</div>
    </div>
    <div class="item" style="left:20px;top:142px;width:266px">
      <div class="item__row">Green Tea Ice cream<span class="item__leader"></span>$4.5</div>
    </div>
  </section>

</div>
</body>
</html>
```